2 Creative Website Banners for Furniture Brand

Morning Tobrasca....
The get a great night sleep banner is complete - we are happy with that one.
Ive uploaded a slightly different concept for the other banner below. This is just something rough ive thrown together. But you can see I have added a curve, a maroon coloured background which is slightly transparent and a big heart in the background....
I do not necessarily want to use this heart image but something a bit like this (a nice graphic, gif etc) but something quite elegant faded in, or perhaps a number of hearts (done in a tasteful way). Also can we keep the typography in the same format as you can see for this one.
Nearly there :)!
Industry/Entity Type
Furniture

```html
<!DOCTYPE html>
<html lang="en">
<head>
<meta charset="utf-8">
<title>Harrowmere Furniture – Bedrooms</title>
<link rel="stylesheet" href="https://fonts.googleapis.com/css2?family=Montserrat:wght@300;400&family=Playfair+Display:wght@400&display=swap">
<style>
  :root{
    --page:#ffffff;
    --nav:#a68f7e;
    --nav-text:#f4ece4;
    --gold:#e3b52c;
    --util-text:#6e6a66;
    --hero-dark:#272526;
    --hero-dark-2:#363233;
    --photo-mauve:#6f6068;
    --photo-deep:#3c3338;
    --photo-grey:#8a8690;
    --maroon:#6e1f36;
    --heart:#f3d9e0;
    --ornament:#b9ab98;
    --white:#ffffff;
    --button:#e1d6c7;
    --button-text:#1f1c1a;
    --taupe:#b6a78f;
    --wish-btn:#c9a36a;
  }
  *{box-sizing:border-box;margin:0;padding:0}
  html,body{width:1200px;height:601px;overflow:hidden;background:var(--page)}
  body{position:relative;font-family:"Montserrat",sans-serif}

  .utility-bar{position:absolute;top:0;left:0;width:1200px;height:31px}
  .brand-name{position:absolute;left:116px;top:-7px;font-size:10px;letter-spacing:4px;color:#b8b2ac}
  .utility-links{position:absolute;left:860px;top:5px;display:flex;gap:17px;align-items:center}
  .utility-link{display:flex;align-items:center;gap:5px;font-size:9.5px;color:var(--util-text);font-weight:300}
  .utility-link svg{display:block}

  .main-nav{position:absolute;top:31px;left:0;width:1200px;height:43px;background:var(--nav);border-bottom:2px solid #8d7868}
  .nav-item{position:absolute;top:0;line-height:41px;font-size:14.5px;color:var(--nav-text);font-weight:400;display:flex;align-items:center;gap:8px;white-space:nowrap}
  .nav-item svg{display:block}

  .hero{position:absolute;top:74px;left:0;width:1200px;height:351px;overflow:hidden}
  .hero-room{position:absolute;left:0;top:0;width:613px;height:351px;background:linear-gradient(100deg,var(--hero-dark) 0%,var(--hero-dark-2) 55%,#2e2b2c 100%)}
  .hero-photo{position:absolute;left:613px;top:0;width:587px;height:351px;background:
    radial-gradient(ellipse at 45% 70%, #a393a0 0%, var(--photo-mauve) 40%, transparent 70%),
    linear-gradient(90deg,var(--photo-deep) 0%,var(--photo-mauve) 30%,#5b5058 65%,var(--photo-grey) 85%,#2b2629 100%)}
  .hero-veil{position:absolute;left:0;top:0;width:1200px;height:351px}
  .hero-copy{position:absolute;left:127px;top:0;width:360px;text-align:center;color:var(--white)}
  .hero-kicker{position:absolute;left:-10px;top:44px;width:380px;font-size:26px;line-height:26px;letter-spacing:7.5px;font-weight:400;white-space:nowrap}
  .ornament{position:absolute;left:7px;width:348px;height:28px;background:var(--ornament);opacity:.85;border-radius:14px}
  .ornament.top{top:78px}
  .ornament.bottom{top:193px}
  .hero-title{position:absolute;left:0;top:104px;width:360px;font-family:"Playfair Display",serif;font-size:94px;letter-spacing:26px;line-height:1;padding-left:26px;font-weight:400}
  .hero-text{position:absolute;left:0;top:228px;width:360px;font-size:15.5px;line-height:18px;font-weight:400}
  .hero-button{position:absolute;left:0;top:267px;width:360px;height:48px;background:var(--button);color:var(--button-text);font-size:20px;line-height:48px;font-weight:400}

  .category-tiles{position:absolute;top:478px;left:0;width:1200px;height:123px}
  .tile{position:absolute;top:0;height:123px;border-radius:6px 6px 0 0;overflow:hidden}
  .tile-intro{left:125px;width:198px;background:var(--taupe);border-radius:0}
  .tile-intro::before{content:"";position:absolute;left:5px;top:5px;right:5px;bottom:-10px;border:1.5px solid #efe8dd}
  .tile-intro span{position:absolute;left:0;top:66px;width:198px;text-align:center;color:var(--white);font-size:22px;letter-spacing:10px;font-weight:300}
  .tile-bedroom-white{left:361px;width:219px;background:linear-gradient(90deg,#eeeeec 0%,#e4e3e0 60%,#1f2a3d 68%,#f2f2f0 75%,#dcdcda 100%)}
  .tile-bedroom-grey{left:607px;width:219px;background:linear-gradient(180deg,#e7e6e4 0%,#dcdbd9 55%,#5e5f63 75%,#6a6b6f 100%)}
  .tile-bedroom-window{left:854px;width:218px;background:linear-gradient(180deg,#cfd2d4 0%,#eef0f0 40%,#e2e3e2 100%)}

  .wishlist-button{position:absolute;left:1142px;top:525px;width:35px;height:35px;background:var(--wish-btn);display:flex;align-items:center;justify-content:center}
</style>
</head>
<body>

<header class="utility-bar">
  <span class="brand-name">HARROWMERE FURNITURE</span>
  <nav class="utility-links" aria-label="Account">
    <span class="utility-link">
      <svg width="14" height="14" viewBox="0 0 14 14"><circle cx="7" cy="7" r="5.5" fill="none" stroke="var(--gold)" stroke-width="1.8"/></svg>
      TRACK ORDER
    </span>
    <span class="utility-link">
      <svg width="16" height="14" viewBox="0 0 16 14"><path d="M8 13 C2 8.5 0.5 6 0.5 4 A3.6 3.6 0 0 1 8 2.6 A3.6 3.6 0 0 1 15.5 4 C15.5 6 14 8.5 8 13Z" fill="var(--gold)"/></svg>
      MY WISHLIST
    </span>
    <span class="utility-link">
      <svg width="15" height="15" viewBox="0 0 15 15"><rect x="1" y="4" width="13" height="10" fill="none" stroke="var(--gold)" stroke-width="1.5"/><path d="M4.5 4 V2.5 A3 2 0 0 1 10.5 2.5 V4" fill="none" stroke="var(--gold)" stroke-width="1.3"/></svg>
      CART ( )
    </span>
  </nav>
</header>

<nav class="main-nav" aria-label="Main">
  <span class="nav-item" style="left:146px">HOME</span>
  <span class="nav-item" style="left:300px">BEDROOM <svg width="10" height="6" viewBox="0 0 10 6"><path d="M1 1 L5 5 L9 1" fill="none" stroke="var(--nav-text)" stroke-width="1.6"/></svg></span>
  <span class="nav-item" style="left:501px">LIVING ROOM <svg width="10" height="6" viewBox="0 0 10 6"><path d="M1 1 L5 5 L9 1" fill="none" stroke="var(--nav-text)" stroke-width="1.6"/></svg></span>
  <span class="nav-item" style="left:726px">DINING ROOM <svg width="10" height="6" viewBox="0 0 10 6"><path d="M1 1 L5 5 L9 1" fill="none" stroke="var(--nav-text)" stroke-width="1.6"/></svg></span>
  <span class="nav-item" style="left:953px">CONTACT <svg width="10" height="6" viewBox="0 0 10 6"><path d="M1 1 L5 5 L9 1" fill="none" stroke="var(--nav-text)" stroke-width="1.6"/></svg></span>
</nav>

<section class="hero">
  <div class="hero-room" role="img" aria-label="Dark moody bedroom with mirrored dresser and lamp"></div>
  <div class="hero-photo" role="img" aria-label="Mauve bedroom with upholstered bed, cushions, throw and mirrored bedside tables"></div>

  <svg class="hero-veil" viewBox="0 0 1200 351" aria-hidden="true">
    <defs>
      <linearGradient id="veil-fade" x1="0" y1="0" x2="1" y2="0">
        <stop offset="0" stop-color="var(--maroon)" stop-opacity=".62"/>
        <stop offset=".8" stop-color="var(--maroon)" stop-opacity=".55"/>
        <stop offset="1" stop-color="var(--maroon)" stop-opacity=".35"/>
      </linearGradient>
      <path id="heart" d="M0 9 C-7 3.5 -9 0 -9 -3 A4.5 4.5 0 0 1 0 -5 A4.5 4.5 0 0 1 9 -3 C9 0 7 3.5 0 9Z"/>
    </defs>
    <path d="M0 0 H600 C680 90 690 250 640 351 H0 Z" fill="url(#veil-fade)"/>
    <path d="M600 0 C680 90 690 250 640 351" fill="none" stroke="var(--heart)" stroke-opacity=".35" stroke-width="1.5"/>
    <g fill="none" stroke="var(--heart)" stroke-width=".6">
      <use href="#heart" transform="translate(300 170) scale(15)" stroke-opacity=".10"/>
      <use href="#heart" transform="translate(60 70) scale(2.6)" stroke-opacity=".22" stroke-width="1"/>
      <use href="#heart" transform="translate(545 95) scale(2)" stroke-opacity=".25" stroke-width="1"/>
      <use href="#heart" transform="translate(70 290) scale(1.8)" stroke-opacity=".2" stroke-width="1"/>
      <use href="#heart" transform="translate(560 290) scale(3)" stroke-opacity=".18" stroke-width="1"/>
    </g>
  </svg>

  <div class="hero-copy">
    <p class="hero-kicker">FIND A LOOK YOU</p>
    <div class="ornament top" role="img" aria-label="Decorative leaf and swirl border"></div>
    <h1 class="hero-title">LOVE</h1>
    <div class="ornament bottom" role="img" aria-label="Decorative leaf and swirl border"></div>
    <p class="hero-text">Lorem ipsum dolor sit amet, consectetur adipiscing elit, sed do eiusmod tempor.</p>
    <div class="hero-button">SHOP BEDROOMS</div>
  </div>
</section>

<section class="category-tiles">
  <div class="tile tile-intro"><span>SHOP BY</span></div>
  <div class="tile tile-bedroom-white" role="img" aria-label="White bedroom with upholstered bed and wardrobe"></div>
  <div class="tile tile-bedroom-grey" role="img" aria-label="Grey buttoned headboard bed below a shelf"></div>
  <div class="tile tile-bedroom-window" role="img" aria-label="Bright bedroom with large windows"></div>
</section>

<div class="wishlist-button">
  <svg width="18" height="16" viewBox="0 0 16 14"><path d="M8 13 C2 8.5 0.5 6 0.5 4 A3.6 3.6 0 0 1 8 2.6 A3.6 3.6 0 0 1 15.5 4 C15.5 6 14 8.5 8 13Z" fill="#ffffff"/></svg>
</div>

</body>
</html>
```